Fatigued and Overloaded by COVID Messages? We need original illustrations to show that.

Everywhere you look there are messages about COVID. That is leading many people to feel fatigued and overloaded by the messages.

We surveyed U.S. adults March 20th - 24th, 2020 and measured message fatigue, information overload, perceived repetition, and perceived exaggeration. Here is how participants responded:

When it comes to coronavirus . . .
55% feel exhausted by all the messages.
54% feel overloaded by the amount of information.
51% feel that the messages are repetitive.
47% feel like messages exaggerate how bad it is.

In other words, almost half of U.S. adults show signs of message fatigue, information overload, perceived message repetition, and perceived message exaggeration.

We will continue to survey 400 adults every week for the next 16 weeks. Each time we will measure message fatigue, information overload, perceived repetition, and perceived exaggeration. We expect that it will increase over time.

What are we looking for? We need innovative and original illustrations that attempt to communicate these findings. The illustrations would visualize message fatigue, information overload, perceived message repetition, and perceived message exaggeration.

What sort of visual are we looking for? Our preference is for an original illustration (or set of illustrations). Our preference is for creative and powerful illustrations, but we are also open to the creative and well-executed infographics.

We need these images fast . We will award monetary prizes to the 3 best designs. If we like more than that, then we might purchase more (e.g., in past contests, we have purchased as many as 30 designs).

What we will need:
(1) The illustrations must be original and we will need the photoshop and/or illustrator files for all artwork. (By original, we mean that the illustrations are 100% created by you. Our organization requires that we utilize only original illustrated work. We have had issues with free imagery being pirated and reposted as free. We sidestep that issue by just having everything created.)

(2) The illustration should say, somewhere: "Based on a survey of 400 U.S. adults conducted March 20 - 24th, 2020."

(3) We will have almost 4 months worth of data by the time this is done. In other words, the illustrations might be able to help us present that weekly data.

(4) We have conducted other Artvendo projects. It might be helpful to examine designs we liked in the past. For example, here is another COVID project we just finished:

https://jobs.artvendo-example.com/job/5162048

Target Market(s)

U.S. adults

Requirements
Must have
• Original illustrations. Mobile friendly design. People will view this on their smartphones.
Nice to have
• A design that we can use to communicate the data across time.

```html
<!DOCTYPE html>
<html lang="en">
<head>
<meta charset="utf-8">
<title>Percent of Information effect</title>
<link rel="stylesheet" href="https://fonts.googleapis.com/css2?family=Montserrat:wght@400;500;600&family=Open+Sans:wght@400;800&display=swap">
<style>
  :root {
    --teal: #4a8a8c;
    --teal-deep: #2f7377;
    --sun: #f2c12e;
    --sun-soft: #f7d35c;
    --pill: #f4c22f;
    --phone: #1d2c33;
    --screen: #ffffff;
    --bubble: #1f6fb8;
    --stat: #fff200;
    --ink: #1a1a1a;
    --alert: #ec1c24;
    --white: #ffffff;
    --skin: #f6d9bd;
  }
  * { margin: 0; padding: 0; box-sizing: border-box; }
  html, body { width: 915px; height: 1200px; overflow: hidden; }
  body { position: relative; background: var(--sun); font-family: "Montserrat", sans-serif; }

  .sky { position: absolute; left: 0; top: 0; width: 915px; height: 596px;
    background: radial-gradient(circle at 20% 35%, var(--teal-deep) 0 18%, transparent 19%),
                radial-gradient(circle at 88% 28%, var(--teal-deep) 0 11%, transparent 12%),
                var(--teal); }
  .ground { position: absolute; left: 0; top: 596px; width: 915px; height: 604px;
    background: radial-gradient(ellipse at 55% 35%, var(--sun-soft) 0 45%, var(--sun) 70%); }

  .title { position: absolute; left: 0; top: 24px; width: 915px; text-align: center;
    color: var(--white); font-weight: 600; font-size: 57px; letter-spacing: -1px; }
  .subtitle { position: absolute; left: 149px; top: 101px; width: 614px; height: 96px;
    background: var(--pill); border-radius: 30px; text-align: center;
    color: var(--ink); font-size: 33px; line-height: 43px; padding-top: 6px; font-weight: 400; }

  .phone { position: absolute; left: 243px; top: 221px; width: 429px; height: 758px;
    background: var(--screen); border: 20px solid var(--phone); border-radius: 56px; }
  .phone-notch { position: absolute; left: 370px; top: 226px; width: 177px; height: 60px;
    background: var(--phone); border-radius: 0 0 22px 22px; }
  .phone-more { position: absolute; left: 428px; top: 897px; width: 60px; display: flex; justify-content: space-between; }
  .phone-more span { width: 11px; height: 11px; border-radius: 50%; background: var(--phone); }

  .stat { position: absolute; width: 320px; height: 101px; background: var(--bubble);
    border-radius: 8px; color: var(--white); }
  .stat-tail { position: absolute; bottom: -27px; width: 28px; height: 28px; }
  .stat-tail.left { left: 24px; }
  .stat-tail.right { right: 24px; }
  .stat-value { position: absolute; top: 7px; height: 87px; background: var(--stat);
    border-radius: 6px; color: var(--ink); font-family: "Open Sans", sans-serif;
    font-weight: 800; font-size: 56px; display: flex; align-items: center; justify-content: center; }
  .stat-label { position: absolute; top: 0; height: 101px; display: flex; align-items: center;
    justify-content: center; text-align: center; font-size: 19px; line-height: 27px;
    font-family: "Open Sans", sans-serif; }

  .stat-exhausted { left: 309px; top: 322px; }
  .stat-exhausted .stat-value { left: 8px; width: 182px; }
  .stat-exhausted .stat-label { left: 190px; width: 120px; }

  .stat-overload { left: 298px; top: 480px; }
  .stat-overload .stat-value { right: 6px; width: 178px; }
  .stat-overload .stat-label { left: 14px; width: 122px; }

  .stat-repetitive { left: 309px; top: 629px; }
  .stat-repetitive .stat-value { left: 8px; width: 163px; }
  .stat-repetitive .stat-label { left: 171px; width: 149px; }

  .stat-exaggerate { left: 298px; top: 776px; }
  .stat-exaggerate .stat-value { right: 6px; width: 132px; }
  .stat-exaggerate .stat-label { left: 40px; width: 140px; }

  .figure { position: absolute; background: radial-gradient(circle, var(--skin) 0 55%, #e9c3a0 100%); border-radius: 50%; }
  .figure-tired { left: 628px; top: 330px; width: 70px; height: 88px; border-radius: 40%; }
  .figure-papers { left: 202px; top: 442px; width: 110px; height: 144px; border-radius: 14px;
    background: linear-gradient(#ececec, var(--skin)); }
  .figure-crowd { left: 629px; top: 640px; width: 153px; height: 88px; border-radius: 44px; }
  .figure-lens { left: 192px; top: 768px; width: 125px; height: 154px; border-radius: 50% 50% 40% 40%;
    background: linear-gradient(160deg, var(--skin) 55%, #2a2a2a 100%); }

  .survey-note { position: absolute; left: 58px; top: 998px; width: 809px; height: 175px;
    background: var(--alert); border-radius: 44px; color: var(--white); text-align: center;
    font-size: 26.5px; line-height: 34px; padding-top: 19px; }
</style>
</head>
<body>
  <div class="sky" role="img" aria-label="Teal background scattered with coronavirus particle illustrations"></div>
  <div class="ground" role="img" aria-label="Yellow map of the United States"></div>

  <h1 class="title">Percent of Information effect</h1>
  <p class="subtitle">to American people<br>When it comes to coronavirus</p>

  <div class="phone"></div>
  <div class="phone-notch"></div>

  <div class="stat stat-exhausted">
    <div class="stat-value">55%</div>
    <div class="stat-label">exhausted by all the messages</div>
    <svg class="stat-tail left" viewBox="0 0 28 28"><path d="M0 0 H28 L0 28 Z" fill="var(--bubble)"/></svg>
  </div>
  <div class="figure figure-tired" role="img" aria-label="Exhausted cartoon character with an empty battery"></div>

  <div class="stat stat-overload">
    <div class="stat-label">information overload</div>
    <div class="stat-value">54%</div>
    <svg class="stat-tail right" viewBox="0 0 28 28"><path d="M0 0 H28 V28 Z" fill="var(--bubble)"/></svg>
  </div>
  <div class="figure figure-papers" role="img" aria-label="Cartoon character buried under a pile of papers"></div>

  <div class="stat stat-repetitive">
    <div class="stat-value">51%</div>
    <div class="stat-label">the messages are repetitive</div>
    <svg class="stat-tail left" viewBox="0 0 28 28"><path d="M0 0 H28 L0 28 Z" fill="var(--bubble)"/></svg>
  </div>
  <div class="figure figure-crowd" role="img" aria-label="Three repeated cartoon characters in a row"></div>

  <div class="stat stat-exaggerate">
    <div class="stat-label">messages exaggerate how bad it is</div>
    <div class="stat-value">47%</div>
    <svg class="stat-tail right" viewBox="0 0 28 28"><path d="M0 0 H28 V28 Z" fill="var(--bubble)"/></svg>
  </div>
  <div class="figure figure-lens" role="img" aria-label="Cartoon character magnified under a magnifying glass"></div>

  <div class="phone-more"><span></span><span></span><span></span></div>

  <p class="survey-note">We surveyed 400 U.S. adults March 20th - 24th, 2020<br>Measured message fatigue,<br>information overload, perceived repetition,<br>and perceived exaggeration.</p>
</body>
</html>
```